TALMERA Stationary and Biz Card design
TALMERA Economic Development Company
TALMERA Stationary and Biz Card design - Financial Services
Creative Brief
Professional
Dennis P Wexford
CEO
PO BOX 782 FAIRHOLT, MAINE 04987
dennis@talmeraco.example
talmeraco.example
Looking for designs that encompass the strength and integrity of the logo.

```html
<!DOCTYPE html>
<html lang="en">
<head>
<meta charset="utf-8">
<title>TALMERA Business Card</title>
<link rel="stylesheet" href="https://fonts.googleapis.com/css2?family=Open+Sans:wght@400;600;700&display=swap">
<style>
  :root {
    --backdrop: #e9e6e1;
    --card: #ffffff;
    --brand-blue: #1b5b94;
    --ink: #1f1f1f;
    --brand-grey: #5e6772;
  }
  html, body {
    margin: 0;
    padding: 0;
    width: 1200px;
    height: 778px;
    overflow: hidden;
    background: var(--backdrop);
    font-family: "Open Sans", Arial, sans-serif;
  }
  .card {
    position: absolute;
    left: 60px;
    top: 85px;
    width: 1080px;
    height: 608px;
    background: var(--card);
    border-radius: 28px;
    overflow: hidden;
    box-shadow: 0 4px 14px rgba(0,0,0,0.18);
  }
  .brand {
    position: absolute;
    left: 55px;
    top: 140px;
    width: 360px;
    display: flex;
    align-items: center;
    justify-content: center;
    gap: 16px;
  }
  .brand-dot {
    width: 22px;
    height: 22px;
    border-radius: 50%;
    background: var(--brand-blue);
  }
  .brand-name {
    font-weight: 600;
    font-size: 58px;
    letter-spacing: 8px;
    color: var(--brand-grey);
  }
  .holder {
    position: absolute;
    right: 70px;
    top: 48px;
    text-align: right;
  }
  .holder-name {
    font-weight: 700;
    font-size: 31px;
    color: var(--brand-blue);
    margin: 0;
    line-height: 1.2;
  }
  .holder-title {
    font-weight: 700;
    font-size: 20px;
    color: var(--ink);
    margin: 4px 0 0;
  }
  .side-tab {
    position: absolute;
    left: 0;
    top: 306px;
    width: 30px;
    height: 166px;
    background: var(--brand-blue);
    border-radius: 0 14px 14px 0;
  }
  .contact {
    position: absolute;
    left: 58px;
    top: 308px;
    margin: 0;
    padding: 0;
    list-style: none;
    font-size: 21px;
    color: var(--ink);
    line-height: 33px;
  }
  .contact li {
    display: flex;
    align-items: center;
    gap: 10px;
    height: 33px;
  }
  .contact svg {
    width: 16px;
    height: 16px;
    fill: var(--ink);
    flex: none;
  }
</style>
</head>
<body>
  <main class="card">
    <div class="brand">
      <span class="brand-dot"></span>
      <span class="brand-name">TALMERA</span>
    </div>

    <header class="holder">
      <h1 class="holder-name">Dennis P Wexford</h1>
      <p class="holder-title">CEO</p>
    </header>

    <div class="side-tab"></div>

    <ul class="contact">
      <li>PO BOX 782</li>
      <li>Fairholt, Maine 04987</li>
      <li>
        <svg viewBox="0 0 16 16" aria-hidden="true"><rect x="4" y="1" width="8" height="14" rx="1.5"/><rect x="5.5" y="3" width="5" height="8" fill="#fff"/></svg>
        310 555 0147
      </li>
      <li>
        <svg viewBox="0 0 16 16" aria-hidden="true"><rect x="1" y="6" width="14" height="8" rx="1"/><rect x="4" y="2" width="8" height="5" fill="none" stroke="#1f1f1f" stroke-width="1.5"/><rect x="4" y="9" width="8" height="1.5" fill="#fff"/></svg>
        207 555 0193
      </li>
      <li>
        <svg viewBox="0 0 16 16" aria-hidden="true"><rect x="1" y="3" width="14" height="10" fill="none" stroke="#1f1f1f" stroke-width="1.5"/><path d="M1.5 3.5 L8 9 L14.5 3.5" fill="none" stroke="#1f1f1f" stroke-width="1.5"/></svg>
        dennis@talmeraco.example
      </li>
      <li>
        <svg viewBox="0 0 16 16" aria-hidden="true"><circle cx="8" cy="8" r="7"/><path d="M1 8 H15 M8 1 C4 5 4 11 8 15 M8 1 C12 5 12 11 8 15" fill="none" stroke="#fff" stroke-width="1.2"/></svg>
        www.talmeraco.example
      </li>
    </ul>
  </main>
</body>
</html>
```